Northern Summit Builders & Affiliates Redesigning our Look

We need stationary (letterhead, envelopes, notepads, invoicing templates, etc) that all coordinate. We are an commerial and residential exteriors construction company that operates 3 companies which all run exclusively, however, the compliment one another well.

Northern Summit Builders (this company installs exteriors on jobsites both residential and commercial)
Northern Summit Roofing & Building Supply (this company sells exterior building materials to homeowners and builders.)
Northern Summit Dumpster Services (This company delivers roll away dumpster cans to homeowners and builders)

Just a note: When I say we do exterior work. We do roofing, siding, stone, windows/doors, gutters, and decks.

We are looking for stationary that includes all three and keeps with our patriotic theme

Info on our firm:
Address: 2718 Tamarind Rd, Elkton MI 48512
Phone: 231-555-0172
Website: www.northernsummit-example.us

Target Market(s)

Our companies target market is vast. We work in the B2B space as well as with homeowner (retail customers). We are in the home and commercial buiding construction field. We specialized in exteriors. (Roofing, Siding, Stone, Windows, Doors, Decks, Gutters)

Industry/Entity Type

Construction

Colors
ec1f27
ffffff
0555a3

Requirements
Must have
• Would like to have a clean professional look with a patriotic theme
Nice to have
• Red/White/Blue

```html
<!DOCTYPE html>
<html lang="en">
<head>
<meta charset="utf-8">
<title>Northern Summit Stationery</title>
<link href="https://fonts.googleapis.com/css2?family=Poppins:wght@400;600&display=swap" rel="stylesheet">
<style>
:root{
  --backdrop:#d2d2d2;
  --paper:#f0f0f0;
  --red:#ec1f27;
  --navy:#14164a;
  --ink:#1a1a1a;
  --grey:#555;
  --faint:#e6e6e6;
}
*{box-sizing:border-box;margin:0;padding:0}
html,body{width:1200px;height:1041px;overflow:hidden}
body{background:var(--backdrop);font-family:"Poppins",sans-serif;color:var(--ink);position:relative}
.sheet{position:absolute;background:var(--paper);box-shadow:0 1px 3px rgba(0,0,0,.18)}
.art{position:absolute}
.art-flag{background:linear-gradient(90deg,var(--navy) 0 33%,transparent 33%),repeating-linear-gradient(180deg,var(--red) 0 9%,var(--paper) 9% 18%);}
.art-faint{background:linear-gradient(100deg,var(--faint),#ececec 60%,rgba(240,240,240,0))}
.brand{position:absolute;font-weight:600;line-height:1;color:var(--ink);letter-spacing:-.02em;display:flex;align-items:center;gap:6px}
.brand .mark{width:.55em;height:.55em;background:var(--red)}
.brand.light{color:#fff}
.division{font-size:5.5px;line-height:1.35;color:var(--grey);padding-left:5px;border-left:1px solid var(--red);margin-bottom:10px}
.division b{display:block;color:var(--ink);font-weight:600}
.divisions-right .division{text-align:right;border-left:0;border-right:1px solid var(--red);padding:0 5px 0 0}
.navy-rule .division{border-color:var(--navy)}
.small{font-size:5px;line-height:1.5;color:var(--grey)}
.small b{color:var(--red);font-weight:400}
/* folder */
.folder{left:166px;top:76px;width:417px;height:541px;border-radius:3px}
.folder .spine{position:absolute;left:24px;top:0;bottom:0;border-left:1px solid #dcdcdc}
/* letterhead */
.letterhead{left:615px;top:95px;width:403px;height:522px}
.letterhead .foot{position:absolute;left:28px;right:28px;top:489px;border-top:1px solid #ddd;padding-top:5px;display:flex;justify-content:space-between}
/* envelopes */
.envelope-front{left:132px;top:645px;width:451px;height:196px}
.envelope-back{left:615px;top:645px;width:451px;height:196px}
.envelope-front .row{position:absolute;left:20px;right:24px;bottom:12px;display:flex;justify-content:space-between;align-items:flex-end}
.envelope-front .row .division{margin:0}
/* cards */
.card-front{left:416px;top:870px;width:167px;height:96px;background:var(--navy)}
.card-front .division{color:#c9cadb;border:0;border-right:1px solid var(--red);text-align:right;padding:0 4px 0 0;margin-bottom:5px;font-size:4px}
.card-front .division b{color:#fff}
.card-back{left:615px;top:870px;width:167px;height:96px}
.card-back .division{font-size:3.8px;margin:0}
</style>
</head>
<body>

<section class="sheet folder">
  <div class="art art-flag" role="img" aria-label="Brush-stroke American flag artwork" style="left:0;top:0;width:417px;height:296px;border-radius:3px 3px 0 0;opacity:.95"></div>
  <div class="spine"></div>
  <div style="position:absolute;left:50px;top:460px">
    <div class="division"><b>Northern Summit</b>Builders</div>
    <div class="division"><b>Northern Summit</b>Roofing &amp; Building Supply</div>
    <div class="division"><b>Northern Summit</b>Dumpster Services</div>
  </div>
  <div class="brand" style="right:30px;top:480px;font-size:22px;flex-direction:column;align-items:flex-end">Northern<span>Summit</span></div>
</section>

<section class="sheet letterhead">
  <div class="brand" style="left:30px;top:28px;font-size:17px;flex-direction:column;align-items:flex-start;gap:2px"><span>Northern</span><span>Summit</span></div>
  <div class="divisions-right" style="position:absolute;right:28px;top:28px">
    <div class="division"><b>Northern Summit</b>Builders</div>
    <div class="division"><b>Northern Summit</b>Roofing &amp; Building Supply</div>
    <div class="division"><b>Northern Summit</b>Dumpster Services</div>
  </div>
  <div class="art art-faint" role="img" aria-label="Faint brush-stroke flag watermark" style="left:0;top:153px;width:403px;height:280px"></div>
  <div class="foot">
    <p class="small">· 2718 Tamarind Rd, Elkton MI 48512 · <b>T:</b> 231-555-0172<br>· 5406 Alder Road, Fenwick MI 48834 · <b>T:</b> 844.555.0198</p>
    <p class="small" style="align-self:center">www.<b>northernsummit-example</b>.us</p>
  </div>
</section>

<section class="sheet envelope-front">
  <div class="art art-faint" role="img" aria-label="Faint brush-stroke flag watermark" style="left:172px;top:0;width:279px;height:124px"></div>
  <div class="brand" style="left:22px;top:18px;font-size:15px;flex-direction:column;align-items:flex-start;gap:2px"><span>Northern</span><span>Summit</span></div>
  <div class="row navy-rule">
    <p class="small" style="border-left:1px solid var(--red);padding-left:4px;margin-right:auto">2718 Tamarind Rd<br>Elkton MI 48512</p>
    <div class="divisions-right" style="display:flex;gap:18px">
      <div class="division"><b>Northern Summit</b>Builders</div>
      <div class="division"><b>Northern Summit</b>Roofing &amp; Building Supply</div>
      <div class="division"><b>Northern Summit</b>Dumpster Services</div>
    </div>
  </div>
</section>

<section class="sheet envelope-back">
  <svg width="451" height="66" style="position:absolute;left:0;top:0" aria-hidden="true">
    <path d="M0 0H451L432 62Q431 65 427 65H24Q20 65 19 62Z" fill="var(--navy)"/>
  </svg>
  <div class="brand light" style="left:0;right:0;top:26px;justify-content:center;font-size:9px">Northern Summit</div>
</section>

<section class="sheet card-front">
  <div class="brand light" style="left:14px;top:26px;font-size:13px;flex-direction:column;align-items:flex-start;gap:2px"><span>Northern</span><span>Summit</span></div>
  <div style="position:absolute;right:12px;top:22px">
    <div class="division"><b>Northern Summit</b>Builders</div>
    <div class="division"><b>Northern Summit</b>Roofing &amp; Building Supply</div>
    <div class="division"><b>Northern Summit</b>Dumpster Services</div>
  </div>
  <p class="small" style="position:absolute;right:12px;bottom:9px;font-size:3.8px;color:#c9cadb">www.<b>northernsummit-example</b>.us</p>
</section>

<section class="sheet card-back">
  <div class="art art-flag" role="img" aria-label="Brush-stroke American flag artwork" style="left:89px;top:0;width:78px;height:62px"></div>
  <div class="brand" style="left:12px;top:16px;font-size:11px;flex-direction:column;align-items:flex-start;gap:1px"><span>Northern</span><span>Summit</span></div>
  <div style="position:absolute;left:12px;bottom:12px;right:8px;display:flex;gap:8px;align-items:flex-start">
    <p style="font-size:5px;font-weight:600;line-height:1.3;margin-right:auto">JORDAN PRYCE<br><span style="font-weight:400;font-size:4px;color:var(--grey)">General Manager</span></p>
    <div class="division">2718 Tamarind Rd<br>Elkton MI 48512<br><span style="color:var(--red)">T:</span> 231-555-0172</div>
    <div class="division">5406 Alder Road<br>Fenwick MI 48834<br><span style="color:var(--red)">T:</span> 844.555.0198</div>
  </div>
</section>

</body>
</html>
```